Soltravex business card

a nice business card with the logo,
Soltravex
Delia Vostrand
Marketing Director
CH-1296 Geneva
Switzerland
+41 79 612 3048
email: Delia.Vostrand@soltravex-mail.net

Target Market(s)

fertilizer business people, very nice and classic business card, normal size, make it nice and funky, try to make it different from the normal boring ones if possible.

Industry/Entity Type

Farming

Number of Pages Required

1 page

Requirements
Must have
• logo, Soltravex, my name - mail and phone number
regular business card size for me to print easy please

```html
<!DOCTYPE html>
<html lang="en">
<head>
<meta charset="utf-8">
<title>Soltravex business card</title>
<link rel="stylesheet" href="https://fonts.googleapis.com/css2?family=Open+Sans:wght@400;600;700&display=swap">
<style>
  :root {
    --lime: #a6ff10;
    --lime-glow: #f4ffd8;
    --stone: #939d9a;
    --ink-line: #3a3a3a;
    --paper: #ffffff;
  }
  * { margin: 0; padding: 0; box-sizing: border-box; }
  html, body {
    width: 1200px;
    height: 1200px;
    overflow: hidden;
    background: var(--paper);
    font-family: "Open Sans", Arial, sans-serif;
  }
  .canvas {
    position: relative;
    width: 1200px;
    height: 1200px;
  }
  .card {
    position: absolute;
    top: 250px;
    width: 400px;
    height: 700px;
  }
  .card--front {
    left: 144px;
    border: 1px solid var(--ink-line);
    background: var(--paper);
  }
  .card--back {
    left: 657px;
    background: radial-gradient(ellipse 150px 240px at 50% 50%, var(--lime-glow) 0%, #d8ff84 40%, var(--lime) 100%);
    display: flex;
    align-items: center;
    justify-content: center;
  }
  .brand-mark {
    position: absolute;
    left: 130px;
    top: 105px;
    width: 140px;
    height: 140px;
    border-radius: 50%;
    background: var(--lime);
  }
  .brand-name {
    position: absolute;
    left: 0;
    right: 0;
    top: 328px;
    text-align: center;
    font-size: 19px;
    font-weight: 600;
    letter-spacing: 0.72em;
    padding-left: 0.72em;
    color: var(--stone);
  }
  .contact {
    position: absolute;
    left: 26px;
    top: 430px;
    font-size: 21px;
    line-height: 30px;
    color: var(--stone);
  }
  .contact__name {
    color: var(--lime);
    font-weight: 700;
  }
  .contact__company {
    margin-top: 30px;
    font-weight: 700;
  }
  .back-name {
    font-size: 26px;
    font-weight: 600;
    letter-spacing: 0.6em;
    padding-left: 0.6em;
    color: var(--paper);
  }
</style>
</head>
<body>
  <main class="canvas">
    <section class="card card--front">
      <div class="brand-mark"></div>
      <div class="brand-name">SOLTRAVEX</div>
      <div class="contact">
        <p class="contact__name">DELIA VOSTRAND</p>
        <p class="contact__title">Marketing Director</p>
        <p class="contact__company">SOLTRAVEX</p>
        <p>CH-1296 Geneva</p>
        <p>Switzerland</p>
        <p>+41 79 612 3048</p>
        <p>Delia.Vostrand@soltravex-mail.net</p>
      </div>
    </section>
    <section class="card card--back">
      <p class="back-name">SOLTRAVEX</p>
    </section>
  </main>
</body>
</html>
```